3 -4 PAGE GIFT CERTIFICATE REDEMPTION WEBSITE REVAMP

I am revamping the entire website at www.brightperkcentral.net

Will have brand new theme and new logo. Name Of Company:
Bonus Gratuity Dispatch Network
BGDN

OVERVIEW:
I NEED A 3-4 PAGE WEBSITE DESIGNED WITH CHECKOUT MODULE.
My company offers fully brandable and personalizable gift certificates good for travel, vacations, dining rewards, rebates, electronic gifts, etc. and I need to redesign the website where the fulfillment and redemption happens.

So the way it works is a business uses my online platform to create, brand and personalize these gift certificates. The business can brand the certificates in the upper right hand corner of each certificate where the “Compliments Of” area sits with their company logo, website, contact info, etc and can also personalize each individual gift certificate to a specific customer too. SEE EXAMPLE ATTACHED TO BRIEF.

The example I attached to this brief includes a logo which is really just a picture and under it there is 3 lines of text where the business can put a website, phone number and email.

On the left side of the top banner image you will see “Exclusively For”.

So now, after a customer enters their certificate ID #, the branding on the next page must match the Compliments Of area and also must personalize the Sales Page to the customer that is in the Exclusively For” area of the certificate…...

Page 1: LANDING PAGE
CONTENT:

Welcome to the online redemption source for vacation certificates, travel vouchers, digital electronic products, dining incentives, gas and grocery rewards and more!

ENTER YOUR CERTIFICATE ID #
ENTER YOUR EMAIL

Welcome to the online redemption system for vacation certificates, travel vouchers, rebates, digital products, dining incentives, gas and grocery rewards and more!

PLEASE ENTER A VALID CERTIFICATE ID NUMBER TO VIEW THE DETAILS AND TO REDEEM AND ACTIVATE YOUR SPECIAL OFFER.

Also we need a testimonial module ON THIS PAGE AND SALES PAGE

PAGE 2: SALES PAGE FOR OFFER (we will use the 1-4 Night Las Vegas Hotel Stay Certificate)
INSTRUCTIONS EXPLANATION FOR DESIGNER: Every gift certificate has a "Compliments Of Area" in the upper right hand corner....SEE SAMPLE ATTACHED TO BRIEF. On the sales page we also show this to the customer after they enter the code. Every certificate has a Compliments Of area and we will also add "Exclusively For" so the person that is giving the certificate away can specify the name of the recipient so we will also transffer this information over to the SALES PAGE.

CONTENT FOR SALES PAGE:

WELCOME ~~NAME OF PERSON IN EXCLUSIVELY FOR AREA ON CERTIFICATE~~ !!

THIS SPECIAL INCENTIVE OFFER IS COMPLIMENTS OF

~~LOGO THAT IS SEEN ON CERTIFICATE~~
~~TEXT LINE 1~~
~~TEXT LINE 2~~
~~TEXT LINE 3~~

TITLE OF OFFER: STAY & PLAY IN LAS VEGAS FOR UP TO 4 NIGHTS!
There is no doubt that Las Vegas is one of the hottest travel destinations around the world. In fact, some people would even go as far as saying that perhaps it is THE hottest place to visit. Enjoy up to 4 nights of resort/casino accommodations in exciting Las Vegas, NV. Millions of people travel to this exciting city each year to enjoy its thrills. Thanks to the business you received this certificate from, now you can enjoy Las Vegas, NV too!

Features:
*Travel 7 Days A Week
*Stay Your Choice Of Nights (1-4 Nights)
*Good For Two Adults & Two Children
*Pay Just The Taxes & Fees
*Multiple Travel Date Requests Allowed
*Fully Transferable To Another Person
*Just A 30 Days Advance Notice Required
*You Will Have 12 Months To Complete Travel

HOW CAN WE DO THIS?

We contract with the world leading hotel chains and resorts to help them fill their otherwise empty rooms.

We help fill empty rooms which the hotels, resorts and cruise lines turn into additional revenue from other areas of their property and future bookings.

Hotels rarely experience full occupancy, yet they remain open, providing rooms and services at fixed costs. So when hotels give out their rooms by partnering with marketing companies like us, they might miss out on the room fee, but they already didn't have that in the first place, at least now they have the opportunity to gain a customer for their in-house restaurants, room service, their casinos, an extra day stay, future bookings, etc.

The magic of why our program works so well is the fact that it’s a win win for everyone involved. You win because you received a huge savings. The business who gave you the certificate wins because now you will remember them the next time you need the same kind of product or service that they provide and you might even refer your friends and family members. The hotels and resorts win because they gain additional revenue from other areas of their establishment that they otherwise would not have been able to get and they also have a new client that may book with them in the future. Remember, they didn’t have anyone in the room in the first place so since you are paying the normal rack rate you might be more inclined to spend your money at the hotel. You are never under any obligation to do so though!

Retail Value: Up to $826.00 (based on $159.00 per night)

How it Works:
You will receive up to 4 nights in a 3 star or better Las Vegas resort and casino for up to 4 travelers, 2 adults and 2 children.

Simply redeem the certificate to activate the travel period for 1 year. This means you will have at least 1 year to travel from the date you redeem and activate your offer. Be sure to redeem your certificate before it expires! All certificates will have an accompanying expiration date attached to them.

When you are ready to book you will simply have to pay the daily room rate taxes and fees of approximately $12-$33 per night (not per person). On average the taxes and fees come out to about $19 per night. (Retail Value: Up to $826.00 based on $159.00 per night)

Step 1: Redeem your certificate to activate your offer

Step 2: Fill out the online reservation request form with travel dates within the next 12 months.

Step 3: Wait for a confirmation of your booked reservation. You will be notified immediately upon us booking your reservation.

Go on your vacation and thank the business who gave you this special offer by doing business with them again and referring your friends and family members!

No timeshares or sales presentations, Guaranteed!

PAGE 3 IS CHECKOUT PAGE:

PLEASE USE ****HERE IS SAMPLE CODE FOR YOU TO TEST OUT AT CURRENT REDEMPTION PROCESS WWW.BRIGHTPERKCENTRAL.NET 40613-27149

TO SEE THE CURRENT CHECK OUT. I NEED ALL THE SAME CONTENT JUST A DIFFERENT MORE EFFICIENT CHECKOUT PROCESS HERE. OMIT THE LEFT SIDE OF THE CURRENT CHECK OUT PROCESS AS THIS CURRENT PROCESSS IS ONE STEP AND DOES NOT HAVE A SALES PAGE BUT NOW I AM CREATING A SALES PAGE BEFORE THE CHECKOUT SO THE BRANDING AND PERSONALIZATION WILL HAPPEN ON THE SALES PAGE….THANK YOU

Target Market(s)

END USERS THAT ARE REDEEMING SPECIAL OFFERS GIFT CERTIFICATES

Industry/Entity Type

Marketing

Number of Pages Required

4 page

Colors

Designer to choose colors to be used in the design.

Requirements
Must have
• OVERVIEW:
• I NEED A 3-4 PAGE WEBSITE DESIGNED WITH CHECKOUT MODULE.
• My company offers fully brandable and personalizable gift certificates good for travel, vacations, dining rewards, rebates, electronic gifts, etc. and I need to redesign the website where the fulfillment and redemption happens.
• So the way it works is a business uses my online platform to create, brand and personalize these gift certificates. The business can brand the certificates in the upper right hand corner of each certificate where the “Compliments Of” area sits with their company logo, website, contact info, etc and can also personalize each individual gift certificate to a specific customer too. SEE EXAMPLE ATTACHED TO BRIEF.
• The example I attached to this brief includes a logo which is really just a picture and under it there is 3 lines of text where the business can put a website, phone number and email.
• On the left side of the top banner image you will see “Exclusively For”.
• So now, after a customer enters their certificate ID #, the branding on the next page must match the Compliments Of area and also must personalize the Sales Page to the customer that is in the Exclusively For” area of the certificate…...
• Page 1: LANDING PAGE
• CONTENT:
• Welcome to the online redemption source for vacation certificates, travel vouchers, digital electronic products, dining incentives, gas and grocery rewards and more!
• ENTER YOUR CERTIFICATE ID #
• ENTER YOUR EMAIL
• Welcome to the online redemption system for vacation certificates, travel vouchers, rebates, digital products, dining incentives, gas and grocery rewards and more!
• PLEASE ENTER A VALID CERTIFICATE ID NUMBER TO VIEW THE DETAILS AND TO REDEEM AND ACTIVATE YOUR SPECIAL OFFER.
• Also we need a testimonial module ON THIS PAGE AND SALES PAGE
• PAGE 2: SALES PAGE FOR OFFER (we will use the 1-4 Night Las Vegas Hotel Stay Certificate)
• INSTRUCTIONS EXPLANATION FOR DESIGNER: Every gift certificate has a "Compliments Of Area" in the upper right hand corner....SEE SAMPLE ATTACHED TO BRIEF. On the sales page we also show this to the customer after they enter the code. Every certificate has a Compliments Of area and we will also add "Exclusively For" so the person that is giving the certificate away can specify the name of the recipient so we will also transffer this information over to the SALES PAGE.
• CONTENT FOR SALES PAGE:
• WELCOME ~~NAME OF PERSON IN EXCLUSIVELY FOR AREA ON CERTIFICATE~~ !!
• THIS SPECIAL INCENTIVE OFFER IS COMPLIMENTS OF
• ~~LOGO THAT IS SEEN ON CERTIFICATE~~
• ~~TEXT LINE 1~~
• ~~TEXT LINE 2~~
• ~~TEXT LINE 3~~
• TITLE OF OFFER: STAY & PLAY IN LAS VEGAS FOR UP TO 4 NIGHTS!
• There is no doubt that Las Vegas is one of the hottest travel destinations around the world. In fact, some people would even go as far as saying that perhaps it is THE hottest place to visit. Enjoy up to 4 nights of resort/casino accommodations in exciting Las Vegas, NV. Millions of people travel to this exciting city each year to enjoy its thrills. Thanks to the business you received this certificate from, now you can enjoy Las Vegas, NV too!
• Features:
• *Travel 7 Days A Week
• *Stay Your Choice Of Nights (1-4 Nights)
• *Good For Two Adults & Two Children
• *Pay Just The Taxes & Fees
• *Multiple Travel Date Requests Allowed
• *Fully Transferable To Another Person
• *Just A 30 Days Advance Notice Required
• *You Will Have 12 Months To Complete Travel
• HOW CAN WE DO THIS?
• We contract with the world leading hotel chains and resorts to help them fill their otherwise empty rooms.
• We help fill empty rooms which the hotels, resorts and cruise lines turn into additional revenue from other areas of their property and future bookings.
• Hotels rarely experience full occupancy, yet they remain open, providing rooms and services at fixed costs. So when hotels give out their rooms by partnering with marketing companies like us, they might miss out on the room fee, but they already didn't have that in the first place, at least now they have the opportunity to gain a customer for their in-house restaurants, room service, their casinos, an extra day stay, future bookings, etc.
• The magic of why our program works so well is the fact that it’s a win win for everyone involved. You win because you received a huge savings. The business who gave you the certificate wins because now you will remember them the next time you need the same kind of product or service that they provide and you might even refer your friends and family members. The hotels and resorts win because they gain additional revenue from other areas of their establishment that they otherwise would not have been able to get and they also have a new client that may book with them in the future. Remember, they didn’t have anyone in the room in the first place so since you are paying the normal rack rate you might be more inclined to spend your money at the hotel. You are never under any obligation to do so though!
• Retail Value: Up to $826.00 (based on $159.00 per night)
• How it Works:
• You will receive up to 4 nights in a 3 star or better Las Vegas resort and casino for up to 4 travelers, 2 adults and 2 children.
• Simply redeem the certificate to activate the travel period for 1 year. This means you will have at least 1 year to travel from the date you redeem and activate your offer. Be sure to redeem your certificate before it expires! All certificates will have an accompanying expiration date attached to them.
• When you are ready to book you will simply have to pay the daily room rate taxes and fees of approximately $12-$33 per night (not per person). On average the taxes and fees come out to about $19 per night. (Retail Value: Up to $826.00 based on $159.00 per night)
• Step 1: Redeem your certificate to activate your offer
• Step 2: Fill out the online reservation request form with travel dates within the next 12 months.
• Step 3: Wait for a confirmation of your booked reservation. You will be notified immediately upon us booking your reservation.
• Go on your vacation and thank the business who gave you this special offer by doing business with them again and referring your friends and family members!
• No timeshares or sales presentations, Guaranteed!
• PAGE 3 IS CHECKOUT PAGE:
• PLEASE USE ****HERE IS SAMPLE CODE FOR YOU TO TEST OUT AT CURRENT REDEMPTION PROCESS WWW.BRIGHTPERKCENTRAL.NET 40613-27149
• TO SEE THE CURRENT CHECK OUT. I NEED ALL THE SAME CONTENT JUST A DIFFERENT MORE EFFICIENT CHECKOUT PROCESS HERE. OMIT THE LEFT SIDE OF THE CURRENT CHECK OUT PROCESS AS THIS CURRENT PROCESSS IS ONE STEP AND DOES NOT HAVE A SALES PAGE BUT NOW I AM CREATING A SALES PAGE BEFORE THE CHECKOUT SO THE BRANDING AND PERSONALIZATION WILL HAPPEN ON THE SALES PAGE….THANK YOU
Nice to have
• OVERVIEW:
• Page 1: LANDING PAGE
• CONTENT:
• ENTER YOUR EMAIL
• CONTENT FOR SALES PAGE:
• ~~TEXT LINE 1~~
• ~~TEXT LINE 2~~
• ~~TEXT LINE 3~~
• Features:
• *Travel 7 Days A Week
• HOW CAN WE DO THIS?
• How it Works:
Should not have
• OVERVIEW:
• Page 1: LANDING PAGE
• CONTENT:
• ENTER YOUR EMAIL
• CONTENT FOR SALES PAGE:
• ~~TEXT LINE 1~~
• ~~TEXT LINE 2~~
• ~~TEXT LINE 3~~
• Features:
• *Travel 7 Days A Week
• HOW CAN WE DO THIS?
• How it Works:

```html
<!DOCTYPE html>
<html lang="en">
<head>
<meta charset="utf-8">
<title>BrightPerkCentral – Redemption Processing Center</title>
<link rel="stylesheet" href="https://fonts.googleapis.com/css2?family=Poppins:wght@300;400;500;600&display=swap">
<style>
:root{
  --orange:#f26d21;
  --orange-deep:#d95c16;
  --teal:#5bbfcb;
  --teal-light:#a9dde3;
  --ink:#1f1f24;
  --muted:#6b6f78;
  --band:#f3f5f9;
  --footer:#3f4550;
  --white:#ffffff;
}
*{box-sizing:border-box;margin:0;padding:0}
html,body{width:1200px;height:4165px;overflow:hidden}
body{position:relative;font-family:'Poppins',sans-serif;color:var(--ink);background:var(--white)}
.abs{position:absolute}
.btn{position:absolute;background:var(--orange);color:#fff;border-radius:20px;font-size:12px;font-weight:600;display:flex;align-items:center;justify-content:center}
.center{left:0;width:1200px;text-align:center}

/* header */
.site-header{top:0;left:0;width:1200px;height:120px;background:#fff}
.brand{left:128px;top:38px;display:flex;align-items:center;gap:8px}
.brand-mark{width:22px;height:22px;border-radius:50%;background:var(--orange)}
.brand-name{font-size:26px;font-weight:600;color:var(--orange);letter-spacing:-.5px}
.brand-tag{left:160px;top:87px;font-size:10px;color:#333}
.nav{top:52px;left:472px;font-size:12px;color:#555}
.nav span{position:absolute;white-space:nowrap}
.nav .active{color:var(--teal)}
.header-cta{left:872px;top:42px;width:200px;height:36px;font-size:12px}

/* hero */
.hero-photo{top:120px;left:0;width:1200px;height:600px;background:linear-gradient(100deg,#d9d9d6 0%,#cfcfcc 45%,#c7c4c1 60%,#d94a4f 72%,#e2545a 85%,#cfc9c6 100%)}
.hero-waves{top:560px;left:0}
.hero-title{left:128px;top:255px;font-size:34px;font-weight:500;line-height:39px;color:#111}
.hero-text{left:128px;top:343px;width:440px;font-size:11.5px;line-height:19px;color:#444}
.field{position:absolute;left:128px;width:288px;height:37px;border-radius:19px;background:rgba(255,255,255,.75);font-size:11.5px;color:#9a9a9a;padding-left:24px;display:flex;align-items:center}
.go{left:135px;top:528px;width:40px;height:40px;border-radius:50%;background:var(--orange)}

/* intro */
.intro-title{top:825px;font-size:23px;font-weight:500}
.intro-text{top:862px;left:290px;width:620px;text-align:center;font-size:16px;line-height:25px;color:var(--muted);font-weight:300}
.learn{left:536px;top:946px;width:128px;height:36px}
.cards-art{left:340px;top:1015px;width:520px;height:127px;background:linear-gradient(90deg,#1d2a6b,#1e7a44,#eeeeee,#d02b7c,#14a38a,#2449b8,#f4a73a)}

/* partners */
.partners{top:1142px;left:0;width:1200px;height:240px;background:var(--band)}
.partners-note{top:1205px;font-size:12px;color:#333}
.partner{position:absolute;top:1275px;font-size:26px;color:#9aa0a8;font-weight:500;white-space:nowrap}

/* certificates */
.certs{top:1382px;left:0;width:1200px;height:600px;background:linear-gradient(180deg,#4d5f73 0%,#5d6f80 45%,#6b6a63 75%,#5a5249 100%)}
.certs-title{top:1460px;font-size:23px;font-weight:500;color:#fff}
.cert{position:absolute;width:120px;height:120px;border-radius:50%;display:flex;align-items:center;justify-content:center}
.cert-label{position:absolute;width:160px;text-align:center;font-size:12px;color:#fff}
.explore{left:536px;top:1898px;width:128px;height:34px}

/* support */
.support-title{top:2058px;font-size:23px;font-weight:500}
.stat{left:567px;top:2138px;font-size:82px;font-weight:600;color:var(--teal);line-height:1}
.stat-note{left:567px;top:2235px;width:270px;font-size:12px;line-height:19px;color:#555}
.support-line{top:2343px;font-size:12px;color:#555}
.contact{left:536px;top:2381px;width:128px;height:35px}

/* testimonial */
.testi-photo{top:2490px;left:0;width:1200px;height:600px;background:linear-gradient(100deg,#b9a08c 0%,#a8654e 30%,#c9a07f 50%,#a05a6d 70%,#bfa37c 100%)}
.testi-veil{top:2490px;left:0;width:1200px;height:600px;background:rgba(40,30,30,.35)}
.quote-mark{top:2675px;font-size:50px;color:#fff;font-weight:300;line-height:1}
.quote{top:2728px;left:290px;width:620px;text-align:justify;text-align-last:center;font-size:16px;line-height:24px;color:#fff;font-weight:300}
.author{top:2876px;font-size:15px;color:#fff}
.date{top:2902px;font-size:11px;color:#fff}
.arrow{position:absolute;top:2780px;color:#fff;font-size:24px;font-weight:300}

/* design box */
.design-box{left:128px;top:3165px;width:944px;height:240px;background:var(--orange);border-bottom:10px solid #f7a574}
.design-art{left:180px;top:3200px;width:180px;height:155px;border-radius:10px;background:linear-gradient(135deg,var(--orange-deep),#e8641c)}
.design-title{left:416px;top:3212px;font-size:33px;font-weight:500;color:#1a1a1a}
.design-text{left:416px;top:3260px;width:570px;font-size:11.5px;line-height:19px;color:#1a1a1a}
.design-btn{left:416px;top:3322px;width:208px;height:35px;border:1.5px solid #1a1a1a;border-radius:18px;font-size:11.5px;font-weight:600;display:flex;align-items:center;justify-content:center}

/* closing cta */
.cta-photo{top:3480px;left:0;width:1200px;height:330px;background:linear-gradient(100deg,#2f3a4a 0%,#6e6a70 35%,#a38978 55%,#c7a48d 75%,#56627a 100%)}
.cta-title{left:128px;top:3598px;font-size:33px;font-weight:600;line-height:38px;color:#fff}
.cta-btn{left:128px;top:3710px;width:160px;height:32px}

/* footer */
.site-footer{top:3805px;left:0;width:1200px;height:360px;background:var(--footer)}
.f-head{position:absolute;top:3880px;font-size:16px;font-weight:500;color:#fff}
.f-line{position:absolute;font-size:12px;color:#b9bec6;white-space:nowrap}
.f-link{position:absolute;left:641px;font-size:12px;color:#b9bec6}
.social{position:absolute;top:3912px;width:38px;height:38px;border:1.5px solid #b9bec6;border-radius:50%}
.f-rule{top:4110px;left:128px;width:944px;height:1px;background:#5a606b}
.copyright{top:4128px;font-size:11px;color:#b9bec6}
</style>
</head>
<body>

<!-- header -->
<header class="abs site-header">
  <div class="abs brand"><span class="brand-mark"></span><span class="brand-name">BrightPerkCentral</span></div>
  <div class="abs brand-tag">Redemption Processing Center</div>
  <nav class="abs nav">
    <span class="active" style="left:0">Home</span>
    <span style="left:72px">Sale</span>
    <span style="left:132px">Testimonials</span>
    <span style="left:244px">About</span>
    <span style="left:314px">Contact</span>
  </nav>
  <div class="btn header-cta">Design A Gift Certificate</div>
</header>

<!-- hero -->
<div class="abs hero-photo" role="img" aria-label="Red wrapped gift boxes with white ribbon on a grey wooden table"></div>
<svg class="abs hero-waves" width="1200" height="190" viewBox="0 0 1200 190">
  <path d="M0 60 C300 120 520 150 760 110 C950 80 1100 50 1200 40 L1200 190 L0 190Z" fill="var(--teal-light)"/>
  <path d="M0 20 C150 60 260 90 420 110 C640 140 900 120 1200 70 L1200 90 C900 150 650 170 420 150 C250 130 120 90 0 70Z" fill="var(--teal)" opacity=".8"/>
  <path d="M0 100 C260 170 560 210 820 160 C980 130 1100 100 1200 90 L1200 190 L0 190Z" fill="#fff"/>
</svg>
<h1 class="abs hero-title">Welcome to the online<br>redemption source</h1>
<p class="abs hero-text">Please enter a valid certificate id number to view the details and to redeem and activate your special offer.</p>
<div class="field" style="top:403px">Enter your Certificate Id #</div>
<div class="field" style="top:459px">Email Address</div>
<div class="abs go"><svg width="40" height="40" viewBox="0 0 40 40"><path d="M12 20h15M21 14l6 6-6 6" stroke="#fff" stroke-width="2" fill="none" stroke-linecap="round"/></svg></div>

<!-- intro -->
<h2 class="abs center intro-title">Online Redemption System for</h2>
<p class="abs intro-text">vacation certificates, travel vouchers, rebates, digital products, dining in-centives, gas and grocery rewards and more!</p>
<div class="btn learn">Learn More</div>
<div class="abs cards-art" role="img" aria-label="Fan of colourful branded gift cards"></div>

<!-- partners -->
<section class="abs partners"></section>
<p class="abs center partners-note">Our platform is trusted to power the rewards programs of leading companies, including:</p>
<span class="partner" style="left:128px">Norvale</span>
<span class="partner" style="left:268px">Kestrix</span>
<span class="partner" style="left:428px">Harlow</span>
<span class="partner" style="left:610px">Quillon</span>
<span class="partner" style="left:760px">Vantera</span>
<span class="partner" style="left:940px">Skylane</span>

<!-- certificates -->
<section class="abs certs" role="img" aria-label="Collage of world landmarks with an airliner and hot air balloon"></section>
<h2 class="abs center certs-title">Certificates We Offer</h2>

<div class="cert" style="left:328px;top:1525px;background:#4caf23"><svg width="52" height="52" viewBox="0 0 52 52" fill="none" stroke="#fff" stroke-width="2.5"><rect x="8" y="20" width="36" height="24"/><path d="M8 20h36M26 20v24M18 20c-4-8 4-10 8 0M34 20c4-8-4-10-8 0"/></svg></div>
<div class="cert" style="left:540px;top:1525px;background:#e0198c"><svg width="52" height="52" viewBox="0 0 52 52" fill="none" stroke="#fff" stroke-width="2.5" stroke-linejoin="round"><path d="M26 6c2 0 3 2 3 5v9l15 9v4l-15-4v9l5 4v3l-8-2-8 2v-3l5-4v-9L8 33v-4l15-9v-9c0-3 1-5 3-5z"/></svg></div>
<div class="cert" style="left:752px;top:1525px;background:#f56b0d"><svg width="52" height="52" viewBox="0 0 52 52" fill="none" stroke="#fff" stroke-width="2.5" stroke-linejoin="round"><path d="M28 8h16v16L24 44 8 28z"/><circle cx="37" cy="15" r="3"/></svg></div>
<div class="cert-label" style="left:308px;top:1658px">Gift Certificates</div>
<div class="cert-label" style="left:520px;top:1658px">Travel Vouchers</div>
<div class="cert-label" style="left:732px;top:1658px">Rebates</div>

<div class="cert" style="left:328px;top:1702px;background:#9150b4"><svg width="52" height="52" viewBox="0 0 52 52" fill="none" stroke="#fff" stroke-width="2.5"><rect x="12" y="12" width="28" height="20" rx="2"/><path d="M6 38h40l-3 4H9z"/></svg></div>
<div class="cert" style="left:540px;top:1702px;background:#4caf23"><svg width="52" height="52" viewBox="0 0 52 52" fill="none" stroke="#fff" stroke-width="2.5" stroke-linecap="round"><path d="M18 8v12a4 4 0 0 0 8 0V8M22 8v36M34 8c-4 2-5 10-4 16h4v20"/></svg></div>
<div class="cert" style="left:752px;top:1702px;background:#f2a2c9"><svg width="52" height="52" viewBox="0 0 52 52" fill="none" stroke="#fff" stroke-width="2.5" stroke-linejoin="round"><path d="M12 42l8-20 10 10z"/><path d="M30 20l10-10M32 18l8 2M30 20l-2-8"/></svg></div>
<div class="cert-label" style="left:308px;top:1835px">Digital Products</div>
<div class="cert-label" style="left:520px;top:1835px">Dining Incentives</div>
<div class="cert-label" style="left:732px;top:1835px">Grocer Rewards</div>
<div class="btn explore">Explore More</div>

<!-- support -->
<h2 class="abs center support-title">Customer Support</h2>
<svg class="abs" style="left:343px;top:2123px" width="184" height="184" viewBox="0 0 184 184">
  <circle cx="92" cy="92" r="92" fill="var(--teal)"/>
  <circle cx="92" cy="92" r="66" fill="#fff"/>
  <g fill="none" stroke="var(--teal)" stroke-width="4" stroke-linecap="round">
    <circle cx="92" cy="98" r="38"/>
    <path d="M84 52h16M92 52v8M92 98V76M92 98l12 10M60 66l-6-6M124 66l6-6"/>
  </g>
</svg>
<div class="abs stat">98%</div>
<p class="abs stat-note">of all order escalations are resolved within one business day</p>
<p class="abs center support-line">Our customer support team is always ready for action 24/7 through our integrated ticket system.</p>
<div class="btn contact">Contact Us</div>

<!-- testimonial -->
<div class="abs testi-photo" role="img" aria-label="Blurred photo of smiling friends out shopping"></div>
<div class="abs testi-veil"></div>
<svg class="abs" style="left:0;top:2480px" width="1200" height="620" viewBox="0 0 1200 620">
  <path d="M0 0 H1200 V120 C1100 60 900 40 700 60 C450 85 200 40 0 100Z" fill="#fff"/>
  <path d="M640 60 C850 20 1050 50 1200 110 L1200 180 C1050 100 850 70 640 60Z" fill="var(--teal-light)"/>
  <path d="M0 460 C200 420 420 440 600 520 C760 590 980 600 1200 540 V620 H0Z" fill="#fff"/>
  <path d="M0 450 C180 420 380 440 520 500 C380 470 200 470 0 520Z" fill="var(--teal-light)"/>
  <path d="M1200 330 C1180 420 1120 520 1000 580 C1100 560 1170 520 1200 480Z" fill="var(--teal-light)"/>
</svg>
<div class="abs center quote-mark">&#8220;&#8220;</div>
<p class="abs quote">I worked with the travel agency and they were very patient with me as I narrowed down where myself and another friend wanted to travel to. I gave them destinations and in return they gave me prompt responses on what was available and in our budget. Don't hesitate to work with this travel agency ....because I won't!</p>
<div class="abs center author">Marla T.</div>
<div class="abs center date">31st Jan 2020 09:27:24 pm</div>
<div class="arrow" style="left:203px">&#8249;</div>
<div class="arrow" style="left:983px">&#8250;</div>

<!-- design a certificate -->
<section class="abs design-box"></section>
<div class="abs design-art" role="img" aria-label="Line illustration of a gift card"></div>
<h2 class="abs design-title">Design A Gift Certificate</h2>
<p class="abs design-text">Sed ut perspiciatis unde omnis iste natus error sit voluptatem accusantium doloremque laudantium, totam rem aperiam, eaque ipsa quae ab illo inventore veritatis et.</p>
<div class="abs design-btn">Design A Gift Certificate</div>

<!-- closing cta -->
<div class="abs cta-photo" role="img" aria-label="Hands holding a payment card over a laptop keyboard"></div>
<svg class="abs" style="left:0;top:3470px" width="1200" height="140" viewBox="0 0 1200 140">
  <path d="M0 0 H1200 V90 C1000 30 700 10 420 20 C250 25 100 50 0 80Z" fill="#fff"/>
  <path d="M620 15 C850 10 1050 40 1200 90 V140 C1050 80 850 40 620 15Z" fill="var(--teal-light)"/>
</svg>
<h2 class="abs cta-title">Start connecting to the biggest<br>Reward on the planet.</h2>
<div class="btn cta-btn">Let's Get Started</div>

<!-- footer -->
<footer class="abs site-footer"></footer>
<h3 class="f-head" style="left:128px">Have A Question? Contact Us Today!</h3>
<h3 class="f-head" style="left:641px">Quick Link</h3>
<h3 class="f-head" style="left:824px">Get Social</h3>

<svg class="abs" style="left:128px;top:3922px" width="16" height="16" viewBox="0 0 16 16" fill="none" stroke="#b9bec6" stroke-width="1.3"><path d="M3 2l3 1 1 3-2 1c1 2 2 3 4 4l1-2 3 1 1 3c-6 1-12-5-11-11z"/></svg>
<span class="f-line" style="left:156px;top:3920px;font-size:15px">Call. 1-800-555-0142</span>
<svg class="abs" style="left:128px;top:3948px" width="16" height="16" viewBox="0 0 16 16" fill="none" stroke="#b9bec6" stroke-width="1.3"><rect x="2" y="4" width="12" height="9"/><path d="M2 4l6 5 6-5"/></svg>
<span class="f-line" style="left:156px;top:3948px">e. hello@perkdesk.example</span>
<svg class="abs" style="left:128px;top:3986px" width="16" height="16" viewBox="0 0 16 16" fill="none" stroke="#b9bec6" stroke-width="1.3"><path d="M8 15s5-5 5-9a5 5 0 0 0-10 0c0 4 5 9 5 9z"/><circle cx="8" cy="6" r="1.8"/></svg>
<span class="f-line" style="left:156px;top:3986px;color:#dfe2e6">The Perk Exchange Desk</span>
<span class="f-line" style="left:156px;top:4005px">2260 Orchard Row Ste B #118</span>
<span class="f-line" style="left:156px;top:4024px">Fairbrook, CA 90210</span>

<span class="f-link" style="top:3928px">Sale</span>
<span class="f-link" style="top:3952px">Testimonials</span>
<span class="f-link" style="top:3976px">About</span>
<span class="f-link" style="top:4000px">Contact</span>
<span class="f-link" style="top:4024px">Terms</span>

<span class="social" style="left:824px" aria-label="Social profile"></span>
<span class="social" style="left:873px" aria-label="Social profile"></span>
<span class="social" style="left:922px" aria-label="Social profile"></span>
<span class="social" style="left:971px" aria-label="Social profile"></span>

<div class="abs f-rule"></div>
<p class="abs center copyright">©2019 The Perk Exchange Desk. All rights reserved.</p>

</body>
</html>
```